I need a folder to put papers in when I am scheduling patients for surgery. The information is general, such as costs, consent forms etc. The folder is designed to give the patient these papers in a neat manner. The cover of the folder needs to use my brand and perhaps create some interest when it is sitting on their kitchen bench with visitors and family. I'll attach a typical template for a folder. It needs to be stylish, classic and professional, as I am about to operate on the person's eye. <br/>I would like my logo included. I'll also attach a photo which is on my website which might work to wrap around the folder. The website address is bramwelkoske.com.au and you can see the way the image is used there on most of the pages as a banner. My profile photo could possibly used as well. Perhaps on the back, but if it looks strange then that is not necessary. The contact information need not be on the folder. Just Dr Lars Brimwell, Ophthalmic Surgeon. Finally, our brand slogan is. "The world's a beautiful place, see it clearly". This could also be on it. Again, this all needs to be professional looking. <br/>I've attached all our previous design jobs, 2 profile pictures, and the image that I think would work. Please also look at the website. <br/><br/>The second part of the project is to create a business card for my practice manager. Her name is Fiona Pelkrest<br/>It should include<br/>Fiona Pelkrest (BCom)<br/>Practice Manager for Dr Lars Brimwell<br/>Ophthalmic Surgeon <br/><br/>Then all the details which are on our current business card<br/><br/><br/><br/><br/>

Contact Information for Business Card

Just match the business cards I already have, but use the details above

Colors

Designer to choose colors to be used in the design.

```html
<!DOCTYPE html>
<html lang="en">
<head>
<meta charset="utf-8">
<title>Dr Lars Brimwell – Stationery &amp; Surgery Folder</title>
<link href="https://fonts.googleapis.com/css2?family=Open+Sans:wght@400;600;700&display=swap" rel="stylesheet">
<style>
:root{
  --brand:#1f7ac1;
  --brand-deep:#1666a8;
  --brand-light:#3a9ad9;
  --ink:#444a50;
  --muted:#7a8087;
  --paper:#ffffff;
  --stage:#e3e5e7;
  --sunset-top:#5a5f66;
  --sunset-mid:#c9913a;
  --sunset-low:#2b2a28;
}
*{box-sizing:border-box;margin:0;padding:0}
html,body{width:693px;height:1200px;overflow:hidden;background:var(--stage);font-family:"Open Sans",Arial,sans-serif;color:var(--ink)}
.canvas{position:relative;width:693px;height:1200px}

/* shared brand lockup */
.brand-name{color:var(--brand);font-weight:600;white-space:nowrap;line-height:1}
.brand-role{color:var(--brand-deep);font-weight:600;white-space:nowrap}
.brand-cred{color:var(--muted);white-space:nowrap}
.brand-dot{display:inline-block;border-radius:50%;background:var(--brand);vertical-align:middle}

/* letterhead */
.letterhead{position:absolute;left:24px;top:24px;width:216px;height:306px;background:var(--paper);box-shadow:0 2px 6px rgba(0,0,0,.12);overflow:hidden}
.letterhead .lockup{position:absolute;left:16px;top:22px}
.letterhead .brand-name{font-size:10px}
.letterhead .brand-role{font-size:3.6px;margin-top:2px}
.letterhead .brand-cred{font-size:3px}
.contact-mini{position:absolute;right:14px;top:18px;font-size:3.4px;line-height:1.5;color:var(--muted)}
.contact-mini .gap{height:3px}
.letter-body{position:absolute;left:16px;right:16px;top:78px;font-size:4.2px;line-height:1.55;color:var(--ink)}
.letter-body p{margin-bottom:5px}
.sheet-strip{position:absolute;left:0;right:0;bottom:0;height:7px;background:linear-gradient(90deg,var(--brand-deep),var(--brand-light))}

/* folder inside */
.folder-inside{position:absolute;left:256px;top:24px;width:413px;height:306px;box-shadow:0 2px 6px rgba(0,0,0,.14)}
.folder-inside .pattern-panel{position:absolute;left:0;top:0;width:200px;height:100%;background:linear-gradient(135deg,#2a88cb,#1b6fb3)}
.folder-inside .pocket-panel{position:absolute;left:200px;top:0;width:213px;height:100%;background:var(--brand-light)}
.inner-sheet{position:absolute;left:210px;top:10px;width:194px;height:276px;background:var(--paper)}
.inner-sheet .lockup{position:absolute;left:12px;top:18px}
.inner-sheet .brand-name{font-size:8px}
.inner-sheet .brand-role{font-size:3px;margin-top:2px}
.inner-sheet .brand-cred{font-size:2.6px}
.inner-sheet .contact-mini{right:10px;top:16px;font-size:2.8px}
.inner-sheet .letter-body{left:12px;right:12px;top:56px;font-size:3.4px}
.signature-area{display:block;width:26px;height:14px;margin-top:4px;background:linear-gradient(90deg,#eef0f2,#f7f8f9)}
.pocket{position:absolute;left:200px;top:0;width:213px;height:306px}

/* folder cover spread */
.folder-cover{position:absolute;left:24px;top:362px;width:645px;height:400px;box-shadow:0 3px 10px rgba(0,0,0,.18)}
.cover-back,.cover-front{position:absolute;top:0;width:322.5px;height:400px;overflow:hidden}
.cover-back{left:0;background:linear-gradient(160deg,var(--brand-light),var(--brand-deep))}
.cover-front{left:322.5px;background:var(--paper);border-left:1px solid rgba(0,0,0,.06)}
.back-band{position:absolute;inset:0;background:linear-gradient(180deg,#ffffff,#d9dbdd);clip-path:polygon(0 0,100% 0,100% 22%,0 44%)}
.back-title{position:absolute;left:26px;top:70px;transform:rotate(-10deg);transform-origin:left top}
.back-title .brand-name{font-size:30px;font-weight:600}
.back-title .back-role{font-size:12px;font-weight:600;color:var(--muted);margin-top:2px;letter-spacing:.4px}
.portrait{position:absolute;left:10px;bottom:0;width:180px;height:176px;background:radial-gradient(ellipse at 50% 40%,#c9ab95 0,#b49a86 30%,#a79b8e 55%,rgba(31,122,193,0) 75%)}
.cover-front .lockup{position:absolute;left:44px;top:38px;display:flex;align-items:center;gap:8px}
.cover-front .brand-dot{width:22px;height:22px}
.cover-front .brand-name{font-size:19px}
.cover-front .brand-role{font-size:7px;color:var(--muted);margin-top:2px}
.cover-front .brand-cred{font-size:5.5px}
.banner-photo{position:absolute;left:0;right:0;top:110px;bottom:0;background:linear-gradient(180deg,var(--sunset-top) 0,#8a7d6a 30%,var(--sunset-mid) 52%,#6b5236 64%,var(--sunset-low) 100%)}
.slogan{position:absolute;left:0;right:0;top:132px;text-align:center;color:#fff;font-size:13px;font-weight:600;line-height:1.25;letter-spacing:.2px}

/* business cards */
.card{position:absolute;top:800px;width:316px;height:178px;box-shadow:0 2px 6px rgba(0,0,0,.18);overflow:hidden}
.card-contact{left:24px;background:var(--paper)}
.card-brand{left:353px;background:radial-gradient(ellipse at 45% 40%,var(--brand-light),var(--brand-deep) 80%)}
.card-contact .lockup{position:absolute;left:24px;top:24px}
.card-contact .brand-name{font-size:14px}
.card-contact .brand-role{font-size:5.4px;margin-top:3px;color:var(--ink)}
.card-contact .brand-cred{font-size:4.2px}
.person{position:absolute;left:151px;top:82px}
.person .person-name{font-size:10.5px;font-weight:600;color:var(--brand)}
.person .person-title{font-size:7px;line-height:1.3;color:var(--ink)}
.card-lines{position:absolute;left:151px;top:124px;font-size:7.6px;line-height:1.48;color:var(--ink)}
.card-lines .line{display:flex;align-items:center;gap:3px}
.card-lines svg{width:8px;height:8px}
.card-address{position:absolute;left:24px;top:138px;font-size:7.6px;line-height:1.48;color:var(--ink)}
.card-contact .sheet-strip{height:6px}
.card-brand .lockup{position:absolute;left:44px;top:62px;display:flex;align-items:center;gap:10px}
.card-brand .brand-dot{width:26px;height:26px;background:#fff}
.card-brand .brand-name{font-size:19px;color:#fff}
.card-brand .brand-role{font-size:7px;color:#fff;margin-top:3px}
.card-brand .brand-cred{font-size:6px;color:#e6f1fa}

/* envelope */
.envelope{position:absolute;left:188px;top:1010px;width:316px;height:158px;background:var(--paper);box-shadow:0 2px 6px rgba(0,0,0,.14);overflow:hidden}
.envelope .flap{position:absolute;left:0;top:0;width:230px;height:26px;background:var(--brand);border-radius:14px 14px 0 0}
.envelope .lockup{position:absolute;left:18px;top:40px}
.envelope .brand-name{font-size:10px}
.envelope .brand-role{font-size:3.6px;margin-top:2px}
.envelope .brand-cred{font-size:3px}
.envelope .env-address{position:absolute;left:18px;bottom:14px;font-size:3.6px;line-height:1.4;color:var(--muted)}
</style>
</head>
<body>
<main class="canvas">

  <!-- Letterhead -->
  <section class="letterhead" aria-label="Letterhead">
    <div class="lockup">
      <div class="brand-name">Dr Lars Brimwell</div>
      <div class="brand-role">Ophthalmic Surgeon</div>
      <div class="brand-cred">MBBS (Hons) MMed FRANZCO</div>
    </div>
    <div class="contact-mini">
      <div>(08) 9412 5530</div>
      <div>(08) 9412 5531</div>
      <div>reception@bramwelkoske.com.au</div>
      <div class="gap"></div>
      <div>14 Marlowe Ave, Dunsford</div>
      <div>Western Australia 6009</div>
    </div>
    <div class="letter-body">
      <p>Dear customer,</p>
      <p>Lorem ipsum dolor sit amet, consectetur adipisicing elit, sed do eiusmod tempor incididunt ut labore et dolore magna aliqua. Ut enim ad minim veniam, quis nostrud exercitation ullamco laboris nisi ut aliquip ex ea commodo consequat. Duis aute irure dolor in reprehenderit in voluptate velit esse cillum dolore eu fugiat nulla pariatur. Excepteur sint occaecat cupidatat non proident, sunt in culpa qui officia deserunt mollit anim id est laborum.</p>
      <p>Lorem ipsum dolor sit amet, consectetur adipisicing elit, sed do eiusmod tempor incididunt ut labore et dolore magna aliqua. Ut enim ad minim veniam, quis nostrud exercitation ullamco laboris nisi ut aliquip ex ea commodo consequat. Duis aute irure dolor in reprehenderit in voluptate velit esse cillum dolore eu fugiat nulla pariatur.</p>
      <p>Lorem ipsum dolor sit amet, consectetur adipisicing elit, sed do eiusmod tempor incididunt ut labore et dolore magna aliqua. Ut enim ad minim veniam, quis nostrud exercitation ullamco laboris nisi ut aliquip ex ea commodo consequat.</p>
    </div>
    <div class="sheet-strip"></div>
  </section>

  <!-- Folder, opened -->
  <section class="folder-inside" aria-label="Folder interior">
    <div class="pattern-panel" role="img" aria-label="Repeating brand pattern on blue"></div>
    <div class="pocket-panel"></div>
    <div class="inner-sheet">
      <div class="lockup">
        <div class="brand-name">Dr Lars Brimwell</div>
        <div class="brand-role">Ophthalmic Surgeon</div>
        <div class="brand-cred">MBBS (Hons) MMed FRANZCO</div>
      </div>
      <div class="contact-mini">
        <div>(08) 9412 5530</div>
        <div>(08) 9412 5531</div>
        <div>reception@bramwelkoske.com.au</div>
        <div class="gap"></div>
        <div>14 Marlowe Ave, Dunsford</div>
        <div>Western Australia 6009</div>
      </div>
      <div class="letter-body">
        <p>Dear customer,</p>
        <p>Lorem ipsum dolor sit amet, consectetur adipisicing elit, sed do eiusmod tempor incididunt ut labore et dolore magna aliqua. Ut enim ad minim veniam, quis nostrud exercitation ullamco laboris nisi ut aliquip ex ea commodo consequat. Duis aute irure dolor in reprehenderit in voluptate velit esse cillum dolore eu fugiat nulla pariatur.</p>
        <p>Lorem ipsum dolor sit amet, consectetur adipisicing elit, sed do eiusmod tempor incididunt ut labore et dolore magna aliqua. Ut enim ad minim veniam, quis nostrud exercitation ullamco laboris nisi ut aliquip ex ea commodo consequat.</p>
        <p>Lorem ipsum dolor sit amet, consectetur adipisicing elit, sed do eiusmod tempor incididunt ut labore et dolore magna aliqua. Ut enim ad minim veniam, quis nostrud exercitation.</p>
        <p>Yours Sincerely,</p>
        <span class="signature-area" role="img" aria-label="Handwritten signature"></span>
      </div>
    </div>
    <svg class="pocket" viewBox="0 0 213 306" aria-hidden="true">
      <path d="M213 120 L213 306 L60 306 Q52 250 90 232 Z" fill="#2b8ad0"/>
    </svg>
  </section>

  <!-- Folder cover, flat spread -->
  <section class="folder-cover" aria-label="Folder cover">
    <div class="cover-back">
      <div class="back-band"></div>
      <div class="back-title">
        <div class="brand-name">Dr Lars Brimwell</div>
        <div class="back-role">Ophthalmic Surgeon</div>
      </div>
      <div class="portrait" role="img" aria-label="Portrait photograph of Dr Lars Brimwell"></div>
    </div>
    <div class="cover-front">
      <div class="lockup">
        <span class="brand-dot"></span>
        <div>
          <div class="brand-name">Dr Lars Brimwell</div>
          <div class="brand-role">Ophthalmic Surgeon</div>
          <div class="brand-cred">MBBS (Hons) MMed FRANZCO</div>
        </div>
      </div>
      <div class="banner-photo" role="img" aria-label="Photograph of a sunset over the sea with a fishing rod"></div>
      <p class="slogan">The world's a beautiful place,<br>see it clearly</p>
    </div>
  </section>

  <!-- Business card, contact side -->
  <section class="card card-contact" aria-label="Business card, contact side">
    <div class="lockup">
      <div class="brand-name">Dr Lars Brimwell</div>
      <div class="brand-role">Ophthalmic Surgeon</div>
      <div class="brand-cred">MBBS (Hons) MMed FRANZCO</div>
    </div>
    <div class="person">
      <div class="person-name">Fiona Pelkrest (BCom)</div>
      <div class="person-title">Practice Manager for Dr Lars Brimwell<br>Ophthalmic Surgeon</div>
    </div>
    <div class="card-lines">
      <div class="line">
        <svg viewBox="0 0 10 10" aria-hidden="true"><circle cx="5" cy="5" r="5" fill="var(--brand)"/><path d="M3.3 2.6c.4-.3.8 0 1 .5l.3.7-.5.5c.3.7.8 1.2 1.5 1.5l.5-.5.7.3c.5.2.8.6.5 1-.4.6-1 .8-1.6.5A5 5 0 0 1 2.8 4.2c-.3-.6-.1-1.2.5-1.6z" fill="#fff"/></svg>
        (08) 9412 5530
      </div>
      <div class="line">
        <svg viewBox="0 0 10 10" aria-hidden="true"><circle cx="5" cy="5" r="5" fill="var(--brand)"/><rect x="3" y="2.3" width="4" height="2" fill="#fff"/><rect x="2.4" y="4.6" width="5.2" height="3" rx=".5" fill="#fff"/></svg>
        (08) 9412 5531
      </div>
      <div class="line">
        <svg viewBox="0 0 10 10" aria-hidden="true"><circle cx="5" cy="5" r="5" fill="var(--brand)"/><rect x="2.4" y="3.2" width="5.2" height="3.6" fill="#fff"/><path d="M2.4 3.2 5 5.3 7.6 3.2" fill="none" stroke="var(--brand)" stroke-width=".6"/></svg>
        reception@bramwelkoske.com.au
      </div>
    </div>
    <div class="card-address">14 Marlowe Ave, Dunsford<br>Western Australia 6009</div>
    <div class="sheet-strip"></div>
  </section>

  <!-- Business card, brand side -->
  <section class="card card-brand" aria-label="Business card, brand side">
    <div class="lockup">
      <span class="brand-dot"></span>
      <div>
        <div class="brand-name">Dr Lars Brimwell</div>
        <div class="brand-role">Ophthalmic Surgeon</div>
        <div class="brand-cred">MBBS (Hons) MMed FRANZCO</div>
      </div>
    </div>
  </section>

  <!-- Envelope -->
  <section class="envelope" aria-label="Envelope">
    <div class="flap"></div>
    <div class="lockup">
      <div class="brand-name">Dr Lars Brimwell</div>
      <div class="brand-role">Ophthalmic Surgeon</div>
      <div class="brand-cred">MBBS (Hons) MMed FRANZCO</div>
    </div>
    <div class="env-address">14 Marlowe Ave, Dunsford<br>Western Australia 6009</div>
    <div class="sheet-strip"></div>
  </section>

</main>
</body>
</html>
```